rt for guide - bartholomew finch personal speaking/consulting website

custom website for my personal speaking/consulting services brand, you can see the basic site we are using as a placeholder at www.rtforguide.example now. I want to re-position this to more of a personal brand site and have video samples of speaking events, downloadable content, a video blog, and links to podcast. I really like the design of dorianwelk.example and the feature set should be fairly similar to his. I'll begin to compile more stock images etc. to use for sliders like he has done, for now we'll need to use stock imagery or existing photography from my social accounts. You can get a feel for social at all platforms/bfinchbroker i.e. facebook.com/bfinchbroker. the site should be primarily geared toward showcasing speaking/consulting services and content, as well as be flexible to allow for additional downloadables etc. in the future.

Target Market(s)

entrepreneurs and leaders looking to grow themselves, their business, and those they lead.

Coding

Coded - Design and coding required

Number of Pages Required

3 page

Font styles to use
Sans Serif

Colors

Designer to choose colors to be used in the design.

Requirements
Must have
• modern slick design, video blog, podcast feed, registration for people to subscribe to newsletter

```html
<!DOCTYPE html>
<html lang="en">
<head>
<meta charset="utf-8">
<title>Northvale Talks – Bartholomew Finch</title>
<link href="https://fonts.googleapis.com/css2?family=Permanent+Marker&family=Open+Sans:wght@400;600;700&display=swap" rel="stylesheet">
<style>
:root{
  --stage:#e4e5e7;
  --teal:#3f8e9b;
  --teal-deep:#1d4d57;
  --yellow:#f2c21b;
  --ink:#1e1e1e;
  --white:#ffffff;
  --muted:#cfd8da;
  --grey-text:#666666;
}
*{box-sizing:border-box;margin:0;padding:0}
html,body{width:1200px;height:2400px;overflow:hidden}
body{background:radial-gradient(ellipse at center,#f2f2f3 0%,var(--stage) 70%);font-family:"Open Sans",Arial,sans-serif;color:var(--white)}
.page{position:absolute;left:250px;top:10px;width:700px;height:2380px;background:var(--white);box-shadow:0 10px 30px rgba(0,0,0,.25);overflow:hidden}
section,header,footer{position:relative;width:700px}
.marker{font-family:"Permanent Marker","Open Sans",cursive;text-transform:uppercase;letter-spacing:1px;font-weight:400}
.section-title{position:absolute;left:0;right:0;text-align:center;font-size:28px;line-height:36px;white-space:nowrap}
.title-band{position:absolute;left:0;right:0;text-align:center}
.title-band h2{display:inline-block;padding:0 14px;font-size:26px;line-height:34px;white-space:nowrap}
p{font-size:9px;line-height:14px}
.photo{position:absolute}

/* hero */
.hero{height:290px}
.hero .photo{inset:0;background:linear-gradient(160deg,#6d6d6d,#3a3a3a 55%,#1f1f1f)}
.brand{position:absolute;left:26px;top:16px;font-weight:700;font-size:13px;display:flex;align-items:center;gap:6px}
.brand .dot{width:10px;height:10px;background:var(--yellow)}
.nav{position:absolute;right:26px;top:20px;display:flex;gap:16px;font-size:8px;text-transform:uppercase;letter-spacing:.5px}
.hero-title{position:absolute;left:240px;top:112px;width:340px;padding:14px 10px;border:2px solid var(--white);text-align:center;font-size:24px;line-height:32px;white-space:nowrap}

/* about */
.about{height:424px;background:var(--teal)}
.about .section-title{top:20px}
.about .photo{left:90px;top:90px;width:207px;height:170px;background:linear-gradient(180deg,#8a8a8a,#3c3c3c)}
.about-caption{position:absolute;left:90px;top:260px;width:207px;height:42px;background:var(--yellow);color:var(--ink);font-size:8px;line-height:12px;padding:8px 12px;text-align:center;font-weight:600}
.about-copy{position:absolute;left:340px;top:90px;width:310px}
.about-copy p{margin-bottom:10px}
.signature{font-family:"Permanent Marker","Open Sans",cursive;font-size:13px;margin-top:4px}

/* inspiring */
.inspire{height:404px;background:linear-gradient(135deg,var(--teal-deep),#173a42)}
.inspire .frame{position:absolute;left:20px;top:33px;width:660px;height:357px;border:2px solid var(--white)}
.inspire .title-band{top:16px}
.inspire .title-band h2{background:#1c4a53}
.inspire-copy{position:absolute;left:50px;top:90px;width:360px}
.inspire-copy p{margin-bottom:10px}
.btn-outline{display:inline-block;border:1px solid var(--white);font-size:8px;padding:4px 14px;text-transform:uppercase;margin-top:6px}
.inspire .photo{left:445px;top:110px;width:205px;height:200px;background:linear-gradient(135deg,#a8c7d8,#4e7f99 60%,#2e4e63)}

/* videos */
.videos{height:350px;background:var(--white);color:var(--ink)}
.videos .section-title{top:16px}
.video{position:absolute;background:linear-gradient(160deg,#9a9a9a,#4a4a4a)}
.video svg{position:absolute;left:50%;top:50%;transform:translate(-50%,-50%)}
.v1{left:90px;top:70px;width:268px;height:250px}
.v2{left:362px;top:70px;width:256px;height:123px}
.v3{left:362px;top:197px;width:126px;height:123px}
.v4{left:492px;top:197px;width:126px;height:123px}

/* podcast */
.podcast{height:255px;background:linear-gradient(180deg,#2a2a2a,#111)}
.podcast .icon{position:absolute;left:332px;top:38px}
.podcast .section-title{top:90px}
.episodes{position:absolute;left:150px;right:150px;top:160px;display:flex;justify-content:space-between}
.episode{width:120px;text-align:center;font-size:8px;border-top:1px solid var(--white);padding-top:6px;text-transform:uppercase}
.episode span{display:block;color:var(--muted);text-transform:none;margin-top:3px}

/* events */
.events{height:300px;background:var(--white);color:var(--ink)}
.events .section-title{top:14px}
.event{position:absolute;top:62px;width:165px}
.event .photo{position:relative;height:103px;background:linear-gradient(135deg,#6a8fb0,#2f4c66)}
.event-date{font-size:8px;color:var(--teal);font-weight:700;margin-top:8px;border-bottom:1px solid var(--teal);padding-bottom:3px}
.event p{color:var(--grey-text);margin-top:5px;font-size:8px;line-height:12px}
.e1{left:86px}.e2{left:260px}.e3{left:433px}

/* subscribe */
.subscribe{height:41px;background:var(--yellow);color:var(--ink);display:flex;align-items:center;gap:14px;padding:0 60px}
.subscribe strong{font-size:9px;text-transform:uppercase;letter-spacing:.5px;white-space:nowrap}
.subscribe .field{width:220px;height:20px;background:var(--white);font-size:8px;color:#999;padding:4px 8px}
.btn-teal{background:var(--teal);color:var(--white);font-size:8px;padding:5px 16px;text-transform:uppercase;font-weight:700}

/* contact */
.contact{height:288px;background:var(--ink)}
.contact .frame{position:absolute;left:40px;top:24px;width:620px;height:244px;border:2px solid var(--white)}
.contact .title-band{top:8px}
.contact .title-band h2{background:var(--ink);font-size:22px}
.contact-info{position:absolute;left:90px;top:80px;font-size:8px;line-height:18px}
.contact-info h3{font-size:10px;text-transform:uppercase;margin-bottom:6px}
.contact-info div{display:flex;align-items:center;gap:6px}
.form{position:absolute;left:380px;top:70px;width:230px}
.form .field{height:20px;background:var(--white);margin-bottom:8px;font-size:8px;color:#999;padding:4px 8px}
.form .message{height:56px}
.btn-yellow{background:var(--yellow);color:var(--ink);font-size:8px;font-weight:700;text-align:center;padding:5px;text-transform:uppercase}

footer{height:29px;background:var(--white);color:var(--grey-text);font-size:7px;text-align:center;line-height:29px}
</style>
</head>
<body>
<main class="page">

  <header class="hero">
    <div class="photo" role="img" aria-label="Black and white photo of a business meeting around a conference table"></div>
    <div class="brand"><span class="dot"></span>northvale talks</div>
    <nav class="nav"><span>Home</span><span>About</span><span>Videos</span><span>Podcast</span><span>Events</span><span>Contact</span></nav>
    <h1 class="hero-title marker">Manage your<br>business with me</h1>
  </header>

  <section class="about">
    <h2 class="section-title marker">About me</h2>
    <div class="photo" role="img" aria-label="Portrait photo of Bartholomew Finch in a suit"></div>
    <div class="about-caption">Bartholomew Finch, speaker and consultant helping leaders grow their teams</div>
    <div class="about-copy">
      <p>I help entrepreneurs and leaders build stronger businesses through clear strategy, honest coaching and practical tools that work in the real world. My work is about growth that lasts.</p>
      <p>Over the years I have spoken to teams, founders and managers across many industries, sharing lessons learned from building companies and leading people through change.</p>
      <p>Whether you are starting out or scaling up, my goal is simple: give you the mindset and the plan to lead yourself, your business and those you serve.</p>
      <div class="signature">B. Finch</div>
    </div>
  </section>

  <section class="inspire">
    <div class="frame"></div>
    <div class="title-band"><h2 class="marker">Inspiring life with BF</h2></div>
    <div class="inspire-copy">
      <p>Every talk and session is built around one idea: people grow when they are challenged, supported and given a clear path forward to follow.</p>
      <p>From keynote stages to small workshops, I share stories, frameworks and simple habits that help leaders communicate better, decide faster and inspire the people around them.</p>
      <p>Explore my talks, download free guides and join the newsletter to get new lessons every week.</p>
      <span class="btn-outline">Read more</span>
    </div>
    <div class="photo" role="img" aria-label="Photo of an audience applauding at a speaking event"></div>
  </section>

  <section class="videos">
    <h2 class="section-title marker">Watch latest videos</h2>
    <div class="video v1" role="img" aria-label="Video still of a speaker on stage before a crowd"><svg width="36" height="36" viewBox="0 0 36 36"><circle cx="18" cy="18" r="17" fill="#fff" opacity=".9"/><path d="M14 11 L26 18 L14 25Z" fill="#3f8e9b"/></svg></div>
    <div class="video v2" role="img" aria-label="Video still of a workshop session"></div>
    <div class="video v3" role="img" aria-label="Video still of a team discussion"><svg width="30" height="30" viewBox="0 0 36 36"><circle cx="18" cy="18" r="17" fill="#fff" opacity=".9"/><path d="M14 11 L26 18 L14 25Z" fill="#3f8e9b"/></svg></div>
    <div class="video v4" role="img" aria-label="Video still of a coaching conversation"><svg width="30" height="30" viewBox="0 0 36 36"><circle cx="18" cy="18" r="17" fill="#fff" opacity=".9"/><path d="M14 11 L26 18 L14 25Z" fill="#3f8e9b"/></svg></div>
  </section>

  <section class="podcast">
    <svg class="icon" width="36" height="44" viewBox="0 0 36 44" fill="none" stroke="#fff" stroke-width="2">
      <circle cx="18" cy="16" r="4" fill="#fff"/>
      <path d="M10 24 A11 11 0 1 1 26 24"/>
      <path d="M5 29 A17 17 0 1 1 31 29"/>
      <path d="M18 20 V42"/>
    </svg>
    <h2 class="section-title marker">Podcast</h2>
    <div class="episodes">
      <div class="episode">Episode 12<span>Leading through change</span></div>
      <div class="episode">Episode 11<span>Building trust fast</span></div>
      <div class="episode">Episode 10<span>Habits of growth</span></div>
    </div>
  </section>

  <section class="events">
    <h2 class="section-title marker">Events</h2>
    <div class="event e1">
      <div class="photo" role="img" aria-label="Photo of a conference audience"></div>
      <div class="event-date">March 14, 2024</div>
      <p>Leadership summit keynote on growing teams with purpose.</p>
    </div>
    <div class="event e2">
      <div class="photo" role="img" aria-label="Photo of a hand reaching up toward the sky"></div>
      <div class="event-date">April 22, 2024</div>
      <p>Founders workshop on strategy, focus and steady growth.</p>
    </div>
    <div class="event e3">
      <div class="photo" role="img" aria-label="Photo of colleagues talking in an office"></div>
      <div class="event-date">May 9, 2024</div>
      <p>Evening seminar on coaching the people you lead.</p>
    </div>
  </section>

  <section class="subscribe">
    <strong>Subscribe to our newsletter</strong>
    <div class="field">Your email address</div>
    <span class="btn-teal">Submit</span>
  </section>

  <section class="contact">
    <div class="frame"></div>
    <div class="title-band"><h2 class="marker">Get in touch</h2></div>
    <div class="contact-info">
      <h3>Contact us</h3>
      <div><svg width="10" height="10" viewBox="0 0 10 10"><path d="M2 1 L4 1 L5 3 L4 4 Q5 6 6 6 L7 5 L9 6 L9 8 Q5 9 1 3Z" fill="#f2c21b"/></svg>(555) 010-4477</div>
      <div><svg width="10" height="10" viewBox="0 0 10 10"><rect x="1" y="2" width="8" height="6" fill="none" stroke="#f2c21b"/><path d="M1 2 L5 6 L9 2" fill="none" stroke="#f2c21b"/></svg>hello@northvaletalks.example</div>
      <div><svg width="10" height="10" viewBox="0 0 10 10"><path d="M5 9 Q1 5 1 4 A4 4 0 0 1 9 4 Q9 5 5 9Z" fill="#f2c21b"/><circle cx="5" cy="4" r="1.4" fill="#1e1e1e"/></svg>214 Harbor Lane, Suite 5</div>
    </div>
    <div class="form">
      <div class="field">Name</div>
      <div class="field">Email</div>
      <div class="field message">Message</div>
      <div class="btn-yellow">Send</div>
    </div>
  </section>

  <footer>© 2024 Northvale Talks. All rights reserved.</footer>
</main>
</body>
</html>
```